App design for Monitoring/Notifying Patient's Medication

Design of UX for an Android App that helps patients with medications.

Patient should be able to interact with the App to inform that they have taken the medication (tablets and injections) at proper times.
Ability in App to notify the patient for taking medicines or injections at the proper times.
Medicines and injections to be taken multiple times a day.
Notifications can be visual and audio. Audio may include name and dosage info also.

App requirements
Ability for patient to interact with app to inform that medicine and/or injection has been taken.
Ability to show visual/audio notifications at scheduled times if patient has not taken medicine or injection.
Audio may contain name and dosage of medicine.
In order to increase the use of App, please suggest how to add a rewards section. High level intent is to reward patients who have been taking medications as prescribed for a month.
Menu button at the top which will have 3 action buttons:
1- Home : on click of which the user is back on the landing/notification page.
2-On click of which this will lead the user to a details screen where he can view his medication details as to what all medicines and injections he is taking along with the schedules and the next upcoming notification. This page is entirely read only. It may have a button to help the user go back to the landing page.
3-On click of which, this will show a history of his actions taken in the last 30 days, if the user has pushed the button on notification every time he has consumed the medicine. This page is entirely read only. It may have a button to help the user go back to the landing page.

Thus 3 screens have to be designed:
Home Page
Page for Menu Action button 2
Page for Menu Action button 3

The menu button should be available in all the 3 pages.

The app needs to be simple, friendly and lively so that it ignites an interest in the user to use the app. Please note that many users are illiterate.

It has to be designed only for android phones that will have around 5 inche screen with a resolution between 360 x 640 and 1280 x 720 pixels

Target Market(s)

Patients(most of them are illiterate

Industry/Entity Type

Healthcare

Requirements
Must have
• - best use of screen space. minimum click and scrolls.
• - clean and elegant look.
• - basic font styles
• - bright colors.

```html
<!DOCTYPE html>
<html lang="en">
<head>
<meta charset="utf-8">
<title>Medication Reminder – App Screens</title>
<link rel="stylesheet" href="https://fonts.googleapis.com/css2?family=Roboto:wght@400;500;700&display=swap">
<style>
  :root {
    --canvas: #ffffff;
    --ink: #333333;
    --ink-soft: #555555;
    --muted: #9a9a9a;
    --faint: #d0d0d0;
    --line: #e4e4e4;
    --bg-soft: #eef0f2;
    --status: #f5f5f5;
    --blue: #3a9ad6;
    --cyan: #4dd6e6;
    --yellow: #f6c34e;
    --green: #bfe18f;
    --red: #e98585;
    --ok-text: #7cc240;
    --cancel: #e25b5b;
    --speaker: #f2a81d;
    --indigo: #2f3d9e;
    --navbar: #050505;
  }
  * { box-sizing: border-box; margin: 0; padding: 0; }
  html, body { width: 1200px; height: 534px; overflow: hidden; background: var(--canvas); }
  body { font-family: "Roboto", Arial, sans-serif; color: var(--ink); position: relative; }

  .phone { position: absolute; top: 9px; width: 288px; height: 516px; background: var(--bg-soft); overflow: hidden; box-shadow: 0 0 2px rgba(0,0,0,.15); }
  .phone--today { left: 10px; }
  .phone--alert { left: 307px; }
  .phone--meds { left: 605px; }
  .phone--schedule { left: 903px; }

  .status-bar { position: absolute; top: 0; left: 0; right: 0; height: 16px; background: var(--status); display: flex; justify-content: flex-end; align-items: center; gap: 3px; padding-right: 8px; font-size: 8px; color: #444; }
  .status-bar svg { width: 8px; height: 8px; fill: #444; }

  .app-header { position: absolute; top: 16px; left: 0; right: 0; height: 41px; background: #fff; display: flex; align-items: center; padding: 0 12px; font-size: 14px; font-weight: 700; color: #2b2b2b; }
  .app-header .add { position: absolute; right: 11px; top: 10px; width: 20px; height: 20px; }

  .i { display: inline-block; stroke: currentColor; fill: none; stroke-width: 1.6; stroke-linecap: round; stroke-linejoin: round; }

  /* Today summary card */
  .summary { position: absolute; left: 7px; top: 64px; width: 273px; height: 118px; background: #fff; border: 1px solid var(--line); }
  .summary__next { position: absolute; left: 0; top: 0; width: 139px; height: 117px; border-right: 1px solid var(--line); }
  .summary__next .clock { position: absolute; left: 14px; top: 14px; width: 30px; height: 30px; color: var(--blue); stroke-width: 1.8; }
  .summary__label { position: absolute; left: 13px; top: 57px; font-size: 11.5px; color: var(--ink-soft); }
  .summary__time { position: absolute; left: 13px; top: 75px; font-size: 20px; color: #2f2f2f; }
  .summary__cell { position: absolute; top: 0; height: 58px; width: 67px; border-bottom: 1px solid var(--line); text-align: center; font-size: 11px; color: var(--ink-soft); }
  .summary__cell--med { left: 139px; border-right: 1px solid var(--line); }
  .summary__cell--qty { left: 206px; }
  .summary__cell .pill { width: 14px; height: 14px; margin-top: 14px; color: var(--blue); }
  .summary__cell .big { display: block; margin-top: 12px; font-size: 17px; font-weight: 500; color: var(--blue); line-height: 17px; }
  .summary__cell span.lbl { display: block; margin-top: 3px; }
  .summary__progress { position: absolute; left: 139px; top: 58px; width: 134px; height: 59px; }
  .summary__progress svg { position: absolute; left: 14px; top: 8px; width: 44px; height: 44px; }
  .summary__pct { position: absolute; left: 88px; top: 13px; font-size: 16px; font-weight: 500; color: var(--blue); }
  .summary__cap { position: absolute; left: 73px; top: 33px; font-size: 10px; color: var(--ink-soft); }

  .section-title { position: absolute; left: 11px; font-size: 11px; font-weight: 500; color: #3a3a3a; }

  .dose { position: absolute; left: 6px; width: 275px; height: 40px; border-radius: 2px; color: #fff; font-size: 11px; }
  .dose--upcoming { background: var(--yellow); }
  .dose--taken { background: var(--green); }
  .dose--missed { background: var(--red); }
  .dose > * { position: absolute; top: 50%; transform: translateY(-50%); }
  .dose .clock { left: 10px; width: 14px; height: 14px; }
  .dose__time { left: 30px; font-weight: 700; }
  .dose .kind { left: 114px; width: 13px; height: 13px; }
  .dose__name { left: 133px; font-weight: 700; }
  .dose__qty { left: 224px; }
  .dose__qty b { font-size: 15px; font-weight: 500; margin-right: 3px; }
  .dose .flag { left: auto; right: 12px; width: 13px; height: 13px; }

  .tab-bar { position: absolute; left: 0; right: 0; top: 440px; height: 38px; background: #fff; border-top: 1px solid var(--line); display: flex; }
  .tab { flex: 1; text-align: center; color: var(--muted); font-size: 8.5px; }
  .tab svg { width: 14px; height: 14px; margin-top: 7px; display: block; margin-left: auto; margin-right: auto; stroke-width: 1.3; }
  .tab span { display: block; margin-top: 3px; }
  .tab--active { color: var(--blue); font-weight: 500; }
  .accent-line { position: absolute; left: 0; right: 0; top: 478px; height: 2px; background: var(--indigo); }
  .system-nav { position: absolute; left: 0; right: 0; top: 480px; height: 36px; background: var(--navbar); display: flex; justify-content: space-around; align-items: center; padding: 0 30px; }
  .system-nav svg { width: 18px; height: 18px; stroke: #fff; fill: none; stroke-width: 1.8; }

  /* Reminder dialog */
  .scrim { position: absolute; left: 0; top: 0; right: 0; height: 480px; background: rgba(0,0,0,.42); }
  .reminder { position: absolute; left: 27px; top: 153px; width: 237px; height: 119px; background: #fff; border-radius: 2px; box-shadow: 0 2px 6px rgba(0,0,0,.3); }
  .reminder__title { position: absolute; left: 9px; top: 13px; display: flex; align-items: center; gap: 7px; font-size: 13px; color: #333; }
  .reminder__title .clock { width: 18px; height: 18px; color: var(--blue); }
  .reminder__title b { color: var(--blue); font-weight: 700; }
  .reminder .speaker { position: absolute; right: 10px; top: 12px; width: 16px; height: 16px; color: var(--speaker); }
  .reminder__dose { position: absolute; left: 10px; top: 50px; display: flex; align-items: center; font-size: 11.5px; color: #444; }
  .reminder__dose .pill { width: 14px; height: 14px; color: var(--blue); margin-right: 6px; }
  .reminder__dose b { font-size: 16px; font-weight: 500; color: var(--blue); margin: 0 4px 0 16px; }
  .reminder__actions { position: absolute; left: 0; right: 0; top: 82px; height: 37px; border-top: 1px solid var(--line); display: flex; }
  .reminder__btn { flex: 1; display: flex; align-items: center; justify-content: center; gap: 5px; font-size: 9.5px; font-weight: 500; letter-spacing: .2px; }
  .reminder__btn + .reminder__btn { border-left: 1px solid var(--line); }
  .reminder__btn--cancel { color: var(--cancel); }
  .reminder__btn--done { color: var(--ok-text); }
  .reminder__btn svg { width: 12px; height: 12px; stroke-width: 2; }

  /* Medication list */
  .med-card { position: absolute; left: 7px; width: 273px; height: 152px; background: #fff; border: 1px solid var(--line); }
  .med-card__more { position: absolute; right: 8px; top: 2px; font-size: 14px; font-weight: 700; color: #444; letter-spacing: 1px; }
  .med-card__icon { position: absolute; left: 50%; top: 18px; width: 20px; height: 20px; margin-left: -10px; color: var(--blue); }
  .med-card__name { position: absolute; left: 0; right: 0; top: 43px; text-align: center; font-size: 12.5px; color: #333; }
  .med-card__row { position: absolute; left: 0; right: 0; top: 75px; height: 39px; border-top: 1px solid var(--line); border-bottom: 1px solid var(--line); display: flex; }
  .med-card__row > div { flex: 1; display: flex; align-items: center; justify-content: center; gap: 6px; font-size: 11px; color: #444; }
  .med-card__row > div + div { border-left: 1px solid var(--line); }
  .med-card__row .clock { width: 14px; height: 14px; color: var(--blue); }
  .med-card__row b { font-size: 15px; font-weight: 500; color: var(--blue); }
  .med-card__days { position: absolute; left: 14px; right: 14px; top: 114px; height: 37px; display: flex; justify-content: space-between; align-items: center; padding: 0 13px; font-size: 11px; color: var(--faint); }
  .med-card__days .on { color: var(--blue); font-weight: 700; }

  /* Schedule */
  .progress-panel { position: absolute; left: 0; right: 0; top: 57px; height: 152px; background: var(--bg-soft); }
  .progress-panel svg { position: absolute; left: 93px; top: 11px; width: 102px; height: 102px; }
  .progress-panel__pct { position: absolute; left: 0; right: 0; top: 47px; text-align: center; font-size: 19px; font-weight: 500; color: #333; }
  .progress-panel__cap { position: absolute; left: 0; right: 0; top: 71px; text-align: center; font-size: 9.5px; color: #444; }
  .progress-panel__record { position: absolute; left: 0; right: 0; top: 127px; text-align: center; font-size: 10.5px; color: #555; }
  .progress-panel__record b { font-weight: 700; color: #333; }
  .calendar { position: absolute; left: 0; right: 0; top: 209px; height: 231px; background: #fff; }
  .calendar__month { position: absolute; left: 0; right: 0; top: 13px; text-align: center; font-size: 10.5px; color: #555; }
  .calendar__prev, .calendar__next { position: absolute; top: 13px; width: 12px; height: 12px; color: #333; stroke-width: 2; }
  .calendar__prev { left: 12px; }
  .calendar__next { right: 12px; }
  .calendar__weekdays { position: absolute; left: 0; right: 0; top: 52px; display: grid; grid-template-columns: repeat(7, 1fr); text-align: center; font-size: 10.5px; color: #555; }
  .calendar__grid { position: absolute; left: 0; right: 0; top: 79px; display: grid; grid-template-columns: repeat(7, 1fr); grid-auto-rows: 41.6px; }
  .day { position: relative; border: .5px solid var(--line); font-size: 10.5px; color: #444; display: flex; align-items: center; justify-content: center; }
  .day--blank { border: none; }
  .day--done { background: var(--green); border-color: #fff; }
  .day--missed { background: var(--red); border-color: #fff; }
  .day .mark { position: absolute; right: 4px; bottom: 4px; width: 9px; height: 9px; color: #fff; stroke-width: 2; }
</style>
</head>
<body>

<svg width="0" height="0" style="position:absolute" aria-hidden="true">
  <defs>
    <symbol id="clock" viewBox="0 0 24 24"><circle cx="12" cy="12" r="10"/><path d="M12 6v6h5"/></symbol>
    <symbol id="pill" viewBox="0 0 24 24"><g transform="rotate(-40 12 12)"><rect x="3" y="8" width="18" height="8" rx="4"/><path d="M12 8v8"/><path d="M12 8h5a4 4 0 0 1 0 8h-5z" fill="currentColor"/></g></symbol>
    <symbol id="pen" viewBox="0 0 24 24"><path d="M4 20l1-5L16 4l4 4L9 19z"/><path d="M14 6l4 4"/></symbol>
    <symbol id="syringe" viewBox="0 0 24 24"><path d="M18 2l4 4M20 4l-3 3M16 5l3 3L9 18l-3-3z"/><path d="M6 15l-4 7 7-4"/><path d="M11 10l2 2M13 8l2 2"/></symbol>
    <symbol id="check" viewBox="0 0 24 24"><path d="M4 13l5 5L20 6"/></symbol>
    <symbol id="cross" viewBox="0 0 24 24"><path d="M5 5l14 14M19 5L5 19"/></symbol>
    <symbol id="warn" viewBox="0 0 24 24"><path d="M12 2L1 22h22z" fill="currentColor" stroke="none"/><path d="M12 9v6M12 18v1" stroke="#e98585" stroke-width="2.4"/></symbol>
    <symbol id="plus" viewBox="0 0 24 24"><circle cx="12" cy="12" r="10.5"/><path d="M12 7v10M7 12h10"/></symbol>
    <symbol id="speaker" viewBox="0 0 24 24"><path d="M3 9h4l6-5v16l-6-5H3z" fill="currentColor"/><path d="M16 8a5 5 0 0 1 0 8M19 5a9 9 0 0 1 0 14"/></symbol>
    <symbol id="chev-left" viewBox="0 0 24 24"><path d="M15 4l-8 8 8 8"/></symbol>
    <symbol id="chev-right" viewBox="0 0 24 24"><path d="M9 4l8 8-8 8"/></symbol>
    <symbol id="tab-list" viewBox="0 0 24 24"><path d="M3 5l2 2 3-3M3 12l2 2 3-3M3 19l2 2 3-3M11 6h10M11 13h10M11 20h10"/></symbol>
    <symbol id="tab-pill" viewBox="0 0 24 24"><g transform="rotate(-45 12 12)"><rect x="3" y="8" width="18" height="8" rx="4"/><path d="M12 8v8"/></g></symbol>
    <symbol id="tab-cal" viewBox="0 0 24 24"><rect x="3" y="5" width="18" height="16" rx="1"/><path d="M3 10h18M8 3v4M16 3v4M7 14h2M11 14h2M15 14h2M7 17h2M11 17h2M15 17h2"/></symbol>
    <symbol id="sys-back" viewBox="0 0 24 24"><path d="M18 4L5 12l13 8z"/></symbol>
    <symbol id="sys-home" viewBox="0 0 24 24"><circle cx="12" cy="12" r="8.5"/></symbol>
    <symbol id="sys-recent" viewBox="0 0 24 24"><rect x="4" y="4" width="16" height="16"/></symbol>
    <symbol id="s-wifi" viewBox="0 0 24 24"><path d="M12 21L1 8a16 16 0 0 1 22 0z"/></symbol>
    <symbol id="s-cell" viewBox="0 0 24 24"><path d="M22 2v20H2z"/></symbol>
    <symbol id="s-batt" viewBox="0 0 24 24"><path d="M8 2h8v3h3v17H5V5h3z"/></symbol>
    <symbol id="s-alarm" viewBox="0 0 24 24"><circle cx="12" cy="13" r="8" fill="none" stroke="#444" stroke-width="2.5"/><path d="M12 9v4h3" fill="none" stroke="#444" stroke-width="2"/></symbol>
    <linearGradient id="ring-small" x1="0" y1="0" x2="1" y2="1"><stop offset="0" stop-color="#3a9ad6"/><stop offset="1" stop-color="#4dd6e6"/></linearGradient>
    <linearGradient id="ring-large" x1="1" y1="0" x2="0" y2="1"><stop offset="0" stop-color="#3a9ad6"/><stop offset="1" stop-color="#4dd6e6"/></linearGradient>
  </defs>
</svg>

<!-- Screen 1: Today -->
<section class="phone phone--today">
  <div class="status-bar"><svg><use href="#s-alarm"/></svg><svg><use href="#s-wifi"/></svg><svg><use href="#s-cell"/></svg><svg><use href="#s-batt"/></svg><span>16:54</span></div>
  <header class="app-header">Today<svg class="i add" style="color:var(--blue)"><use href="#plus"/></svg></header>

  <div class="summary">
    <div class="summary__next">
      <svg class="i clock"><use href="#clock"/></svg>
      <div class="summary__label">Next dose due</div>
      <div class="summary__time">11:30 am</div>
    </div>
    <div class="summary__cell summary__cell--med"><svg class="i pill"><use href="#pill"/></svg><span class="lbl">Airevo</span></div>
    <div class="summary__cell summary__cell--qty"><span class="big">2</span><span class="lbl">Pills</span></div>
    <div class="summary__progress">
      <svg viewBox="0 0 44 44"><circle cx="22" cy="22" r="18" fill="none" stroke="#eef6fa" stroke-width="5"/><circle cx="22" cy="22" r="18" fill="none" stroke="url(#ring-small)" stroke-width="5" stroke-dasharray="85 113" transform="rotate(-90 22 22)"/></svg>
      <div class="summary__pct">75%</div>
      <div class="summary__cap">Complete</div>
    </div>
  </div>

  <div class="section-title" style="top:204px">Upcoming</div>
  <div class="dose dose--upcoming" style="top:218px"><svg class="i clock"><use href="#clock"/></svg><span class="dose__time">13:00 pm</span><svg class="i kind"><use href="#pen"/></svg><span class="dose__name">Insulin</span><span class="dose__qty"><b>1</b>Dose</span></div>
  <div class="dose dose--upcoming" style="top:262px"><svg class="i clock"><use href="#clock"/></svg><span class="dose__time">14:30 pm</span><svg class="i kind"><use href="#tab-pill"/></svg><span class="dose__name">Paldex</span><span class="dose__qty"><b>2</b>Pills</span></div>

  <div class="section-title" style="top:324px">Previous</div>
  <div class="dose dose--taken" style="top:339px"><svg class="i clock"><use href="#clock"/></svg><span class="dose__time">08:00 am</span><svg class="i kind"><use href="#tab-pill"/></svg><span class="dose__name">Acidra</span><span class="dose__qty"><b>1</b>Pill</span><svg class="i flag" style="stroke-width:2.4"><use href="#check"/></svg></div>
  <div class="dose dose--missed" style="top:383px"><svg class="i clock"><use href="#clock"/></svg><span class="dose__time">14:30 am</span><svg class="i kind"><use href="#tab-pill"/></svg><span class="dose__name">Paldex</span><span class="dose__qty"><b>1</b>Pill</span><svg class="i flag" style="color:#fff"><use href="#warn"/></svg></div>
  <div class="dose dose--taken" style="top:427px"></div>

  <nav class="tab-bar">
    <div class="tab tab--active"><svg class="i"><use href="#tab-list"/></svg><span>Today</span></div>
    <div class="tab"><svg class="i"><use href="#tab-pill"/></svg><span>My Medication</span></div>
    <div class="tab"><svg class="i"><use href="#tab-cal"/></svg><span>Schedule</span></div>
  </nav>
  <div class="accent-line"></div>
  <div class="system-nav"><svg><use href="#sys-back"/></svg><svg><use href="#sys-home"/></svg><svg><use href="#sys-recent"/></svg></div>
</section>

<!-- Screen 2: Today with dose reminder -->
<section class="phone phone--alert">
  <div class="status-bar"><svg><use href="#s-alarm"/></svg><svg><use href="#s-wifi"/></svg><svg><use href="#s-cell"/></svg><svg><use href="#s-batt"/></svg><span>16:54</span></div>
  <header class="app-header">Today<svg class="i add" style="color:var(--blue)"><use href="#plus"/></svg></header>

  <div class="summary">
    <div class="summary__next">
      <svg class="i clock"><use href="#clock"/></svg>
      <div class="summary__label">Next dose due</div>
      <div class="summary__time">11:30 am</div>
    </div>
    <div class="summary__cell summary__cell--med"><svg class="i pill"><use href="#pill"/></svg><span class="lbl">Airevo</span></div>
    <div class="summary__cell summary__cell--qty"><span class="big">2</span><span class="lbl">Pills</span></div>
    <div class="summary__progress">
      <svg viewBox="0 0 44 44"><circle cx="22" cy="22" r="18" fill="none" stroke="#eef6fa" stroke-width="5"/><circle cx="22" cy="22" r="18" fill="none" stroke="url(#ring-small)" stroke-width="5" stroke-dasharray="85 113" transform="rotate(-90 22 22)"/></svg>
      <div class="summary__pct">75%</div>
      <div class="summary__cap">Complete</div>
    </div>
  </div>

  <div class="section-title" style="top:204px">Upcoming</div>
  <div class="dose dose--upcoming" style="top:218px"><svg class="i clock"><use href="#clock"/></svg><span class="dose__time">13:00 pm</span><svg class="i kind"><use href="#pen"/></svg><span class="dose__name">Insulin</span><span class="dose__qty"><b>1</b>Dose</span></div>
  <div class="dose dose--upcoming" style="top:262px"><svg class="i clock"><use href="#clock"/></svg><span class="dose__time">14:30 pm</span><svg class="i kind"><use href="#tab-pill"/></svg><span class="dose__name">Paldex</span><span class="dose__qty"><b>2</b>Pills</span></div>

  <div class="section-title" style="top:324px">Previous</div>
  <div class="dose dose--taken" style="top:339px"><svg class="i clock"><use href="#clock"/></svg><span class="dose__time">08:00 am</span><svg class="i kind"><use href="#tab-pill"/></svg><span class="dose__name">Acidra</span><span class="dose__qty"><b>1</b>Pill</span><svg class="i flag" style="stroke-width:2.4"><use href="#check"/></svg></div>
  <div class="dose dose--missed" style="top:383px"><svg class="i clock"><use href="#clock"/></svg><span class="dose__time">14:30 am</span><svg class="i kind"><use href="#tab-pill"/></svg><span class="dose__name">Paldex</span><span class="dose__qty"><b>1</b>Pill</span><svg class="i flag" style="color:#fff"><use href="#warn"/></svg></div>
  <div class="dose dose--taken" style="top:427px"></div>

  <nav class="tab-bar">
    <div class="tab tab--active"><svg class="i"><use href="#tab-list"/></svg><span>Today</span></div>
    <div class="tab"><svg class="i"><use href="#tab-pill"/></svg><span>My Medication</span></div>
    <div class="tab"><svg class="i"><use href="#tab-cal"/></svg><span>Schedule</span></div>
  </nav>
  <div class="accent-line"></div>
  <div class="scrim"></div>
  <div class="system-nav"><svg><use href="#sys-back"/></svg><svg><use href="#sys-home"/></svg><svg><use href="#sys-recent"/></svg></div>

  <div class="reminder" role="dialog" aria-label="Dose reminder">
    <div class="reminder__title"><svg class="i clock"><use href="#clock"/></svg><span>Your <b>11:30</b> dose is due!</span></div>
    <svg class="i speaker"><use href="#speaker"/></svg>
    <div class="reminder__dose"><svg class="i pill"><use href="#pill"/></svg>Airevo<b>2</b>Pills</div>
    <div class="reminder__actions">
      <div class="reminder__btn reminder__btn--cancel"><svg class="i"><use href="#cross"/></svg>CANCEL</div>
      <div class="reminder__btn reminder__btn--done"><svg class="i"><use href="#check"/></svg>COMPLETE</div>
    </div>
  </div>
</section>

<!-- Screen 3: My Medication -->
<section class="phone phone--meds">
  <div class="status-bar"><svg><use href="#s-alarm"/></svg><svg><use href="#s-wifi"/></svg><svg><use href="#s-cell"/></svg><svg><use href="#s-batt"/></svg><span>16:54</span></div>
  <header class="app-header">My Medication<svg class="i add" style="color:var(--blue)"><use href="#plus"/></svg></header>

  <article class="med-card" style="top:64px">
    <span class="med-card__more">•••</span>
    <svg class="i med-card__icon"><use href="#pill"/></svg>
    <div class="med-card__name">Airevo</div>
    <div class="med-card__row"><div><svg class="i clock"><use href="#clock"/></svg>11:30 am</div><div><b>1</b>Dose</div></div>
    <div class="med-card__days"><span class="on">M</span><span class="on">T</span><span class="on">W</span><span>T</span><span class="on">F</span><span>S</span><span>S</span></div>
  </article>

  <article class="med-card" style="top:224px">
    <span class="med-card__more">•••</span>
    <svg class="i med-card__icon"><use href="#pill"/></svg>
    <div class="med-card__name">Paldex</div>
    <div class="med-card__row"><div><svg class="i clock"><use href="#clock"/></svg>14:00 pm</div><div><b>1</b>Dose</div></div>
    <div class="med-card__days"><span class="on">M</span><span>T</span><span class="on">W</span><span>T</span><span class="on">F</span><span class="on">S</span><span>S</span></div>
  </article>

  <article class="med-card" style="top:384px">
    <span class="med-card__more">•••</span>
    <svg class="i med-card__icon"><use href="#syringe"/></svg>
    <div class="med-card__name">Thyrolan</div>
  </article>

  <nav class="tab-bar">
    <div class="tab"><svg class="i"><use href="#tab-list"/></svg><span>Today</span></div>
    <div class="tab tab--active"><svg class="i"><use href="#tab-pill"/></svg><span>My Medication</span></div>
    <div class="tab"><svg class="i"><use href="#tab-cal"/></svg><span>Schedule</span></div>
  </nav>
  <div class="accent-line"></div>
  <div class="system-nav"><svg><use href="#sys-back"/></svg><svg><use href="#sys-home"/></svg><svg><use href="#sys-recent"/></svg></div>
</section>

<!-- Screen 4: Schedule -->
<section class="phone phone--schedule">
  <div class="status-bar"><svg><use href="#s-alarm"/></svg><svg><use href="#s-wifi"/></svg><svg><use href="#s-cell"/></svg><svg><use href="#s-batt"/></svg><span>16:54</span></div>
  <header class="app-header">Schedule</header>

  <div class="progress-panel">
    <svg viewBox="0 0 102 102"><circle cx="51" cy="51" r="45" fill="none" stroke="#fff" stroke-width="11"/><circle cx="51" cy="51" r="45" fill="none" stroke="url(#ring-large)" stroke-width="11" stroke-linecap="round" stroke-dasharray="212 283" transform="rotate(-90 51 51)"/></svg>
    <div class="progress-panel__pct">75%</div>
    <div class="progress-panel__cap">Complete</div>
    <div class="progress-panel__record">Personal Record: <b>97%</b></div>
  </div>

  <div class="calendar">
    <svg class="i calendar__prev"><use href="#chev-left"/></svg>
    <div class="calendar__month">Jul 2017</div>
    <svg class="i calendar__next"><use href="#chev-right"/></svg>
    <div class="calendar__weekdays"><span>M</span><span>T</span><span>W</span><span>T</span><span>F</span><span>S</span><span>S</span></div>
    <div class="calendar__grid">
      <div class="day day--blank"></div><div class="day day--blank"></div>
      <div class="day">1</div><div class="day">2</div><div class="day">3</div>
      <div class="day day--missed">4<svg class="i mark"><use href="#cross"/></svg></div>
      <div class="day">5</div>

      <div class="day">6</div>
      <div class="day day--done">7<svg class="i mark"><use href="#check"/></svg></div>
      <div class="day day--done">8<svg class="i mark"><use href="#check"/></svg></div>
      <div class="day day--done">9<svg class="i mark"><use href="#check"/></svg></div>
      <div class="day day--done">10<svg class="i mark"><use href="#check"/></svg></div>
      <div class="day day--done">11<svg class="i mark"><use href="#check"/></svg></div>
      <div class="day day--done">12<svg class="i mark"><use href="#check"/></svg></div>

      <div class="day day--done">13<svg class="i mark"><use href="#check"/></svg></div>
      <div class="day day--done">14<svg class="i mark"><use href="#check"/></svg></div>
      <div class="day day--done">15<svg class="i mark"><use href="#check"/></svg></div>
      <div class="day day--done">16<svg class="i mark"><use href="#check"/></svg></div>
      <div class="day day--done">17<svg class="i mark"><use href="#check"/></svg></div>
      <div class="day day--done">18<svg class="i mark"><use href="#check"/></svg></div>
      <div class="day day--missed">19<svg class="i mark"><use href="#cross"/></svg></div>

      <div class="day day--done">21</div>
      <div class="day day--done">22</div>
      <div class="day">23</div><div class="day">24</div><div class="day">25</div><div class="day">26</div><div class="day">27</div>
    </div>
  </div>

  <nav class="tab-bar">
    <div class="tab"><svg class="i"><use href="#tab-list"/></svg><span>Today</span></div>
    <div class="tab"><svg class="i"><use href="#tab-pill"/></svg><span>My Medication</span></div>
    <div class="tab tab--active"><svg class="i"><use href="#tab-cal"/></svg><span>Schedule</span></div>
  </nav>
  <div class="accent-line"></div>
  <div class="system-nav"><svg><use href="#sys-back"/></svg><svg><use href="#sys-home"/></svg><svg><use href="#sys-recent"/></svg></div>
</section>

</body>
</html>
```